Supplement Manufacture needs a label designed

We need a label design done for a patented supplement for pain management. We would like to see designs that include a shade of blue as the main color. We would like the label to be noticeable amongst the crowded field and position our product to be selected based on the beauty of the label. We have attached a label that we created but it is not what we need but it shows the color blue we prefer. Please visit our website for more information. www.brokaleaf.net.

Target Market(s)

Health conscious individuals, Individuals who are looking for 100% all natural supplements.

Industry/Entity Type

Health And Wellness

Font styles to use
Serif

Colors
2f74b4
9bcb3c
f8a142
fbed22

Requirements
Must have
• Must have professional look and fit on 150cc HDPE packer bottle. Must meet US QHW label requirements.

```html
<!DOCTYPE html>
<html lang="en">
<head>
<meta charset="utf-8">
<title>Brokaleaf Neuromuscular Support Label</title>
<link rel="stylesheet" href="https://fonts.googleapis.com/css2?family=Oswald:wght@300;400;500;600;700&family=Montserrat:wght@600;700&family=Comfortaa:wght@700&display=swap">
<style>
  :root {
    --stage: #1f5e93;
    --deep-blue: #0c5a8f;
    --mid-blue: #0a86c6;
    --sky-blue: #13b0ec;
    --muscle-teal: #0f6f8c;
    --brand-green: #9bcb3c;
    --brand-orange: #f8a142;
    --brand-yellow: #fbed22;
    --facts-blue: #1d5d9c;
    --facts-rule: #3a3a3a;
    --white: #ffffff;
  }
  * { box-sizing: border-box; margin: 0; padding: 0; }
  html, body { width: 1200px; height: 810px; overflow: hidden; background: var(--stage); }
  body { position: relative; font-family: "Oswald", sans-serif; }

  .label {
    position: absolute; left: 20px; top: 188px; width: 1160px; height: 433px;
    background: linear-gradient(90deg, var(--deep-blue) 0%, #0e6ca8 35%, var(--mid-blue) 62%, var(--sky-blue) 76%, var(--sky-blue) 100%);
    overflow: hidden; color: var(--white);
  }
  .figure-art {
    position: absolute; left: 150px; top: 0; width: 690px; height: 394px;
    background:
      radial-gradient(ellipse 30% 60% at 78% 45%, rgba(18,120,150,.85), rgba(18,120,150,0) 70%),
      radial-gradient(ellipse 55% 14% at 40% 34%, rgba(15,95,125,.75), rgba(15,95,125,0) 70%),
      radial-gradient(ellipse 55% 12% at 35% 80%, rgba(15,95,125,.75), rgba(15,95,125,0) 70%);
  }

  .usage { position: absolute; left: 41px; top: 32px; width: 330px; font-weight: 300; font-size: 14.5px; line-height: 18px; letter-spacing: -.1px; }
  .usage p { margin-bottom: 10px; }
  .usage strong { font-weight: 500; }

  .maker { position: absolute; left: 40px; top: 278px; font-weight: 500; font-size: 14px; line-height: 18px; }
  .contact { position: absolute; display: flex; align-items: center; gap: 6px; font-weight: 500; }
  .contact svg { flex: none; }
  .contact-phone { left: 40px; top: 355px; font-size: 16px; }
  .contact-web { left: 312px; top: 331px; font-size: 14px; }
  .contact-mail { left: 312px; top: 355px; font-size: 14px; }

  .brand-name { position: absolute; left: 480px; top: 26px; font-family: "Oswald", sans-serif; font-weight: 700; font-size: 52px; line-height: 1; color: var(--brand-green); letter-spacing: 1px; }
  .tagline { position: absolute; left: 482px; top: 115px; font-family: "Comfortaa", sans-serif; font-weight: 700; font-size: 13px; line-height: 19px; color: var(--brand-orange); }

  .key-ingredients { position: absolute; left: 482px; top: 182px; list-style: none; }
  .key-ingredients li { display: flex; align-items: baseline; gap: 8px; height: 22.5px; font-weight: 500; font-size: 15.5px; color: var(--brand-yellow); }
  .key-ingredients small { font-size: 8.5px; font-weight: 500; }
  .key-ingredients svg { align-self: center; }

  .claims { position: absolute; left: 523px; top: 291px; display: flex; gap: 11px; }
  .claim { width: 34px; height: 39px; background: var(--brand-orange); border-radius: 4px; }

  .count { position: absolute; left: 528px; top: 365px; width: 108px; height: 29px; border-radius: 15px 15px 0 0; background: var(--brand-green); text-align: center; font-family: "Montserrat", sans-serif; font-weight: 700; font-size: 13px; line-height: 30px; }
  .count b { font-size: 20px; }

  .facts { position: absolute; left: 801px; top: 33px; width: 325px; height: 304px; background: var(--white); padding: 10px 12px 0 13px; color: var(--facts-blue); }
  .facts h2 { text-align: center; font-weight: 600; font-size: 23px; color: #2a1f1f; letter-spacing: .2px; margin-bottom: 6px; }
  .serving { font-weight: 600; font-size: 15.5px; padding-bottom: 1px; border-bottom: 1.5px solid var(--facts-rule); }
  .facts-row { display: grid; grid-template-columns: 1fr 44px 44px; align-items: end; border-bottom: 1.5px solid var(--facts-rule); font-size: 11.5px; line-height: 16px; padding: 3px 0 2px; }
  .facts-row span:nth-child(2) { text-align: right; }
  .facts-row span:nth-child(3) { text-align: right; }
  .facts-head { font-weight: 600; font-size: 13px; }
  .facts-note { font-size: 11px; margin-top: 6px; }

  .other { position: absolute; left: 801px; top: 349px; font-weight: 500; font-size: 15.5px; }

  .band { position: absolute; left: 0; top: 394px; width: 1160px; height: 39px; background: var(--brand-green); font-family: "Montserrat", sans-serif; font-weight: 700; }
  .band span { position: absolute; top: 0; line-height: 39px; transform: translateX(-50%); white-space: nowrap; }
  .band-natural { left: 190px; font-size: 17px; letter-spacing: 1px; }
  .band-type { left: 580px; font-size: 17px; }
  .band-patent { left: 965px; font-size: 15px; letter-spacing: 1px; }
</style>
</head>
<body>
<section class="label">
  <div class="figure-art" role="img" aria-label="Illustration of a muscular human figure in motion over a faceted blue background"></div>

  <div class="usage">
    <p><strong>SUGGESTED USE:</strong> 1 to 2 capsules in morning and high, not to exceed 6 capsules per day.</p>
    <p>Do not use if full-bottle shrink-wrap is broken or missing.</p>
    <p>Store in cool, dry place (59oF - 85oF) away from direct light.</p>
    <p><strong>KEEP OUT REACH OF CHILDREN.</strong></p>
    <p>This product was made in a QHW and GMP 9001:2000 registered facility.</p>
    <p>The statements have not been evaluated by the Food and Drug Administration. This product is not intended to diagnose, cure, or prevent any disease.</p>
  </div>

  <div class="maker">Manufatured for:<br>Corvella, LLC<br>Linwood, GA 30512</div>

  <div class="contact contact-phone">
    <svg width="18" height="18" viewBox="0 0 24 24" fill="none" stroke="#fbed22" stroke-width="2"><path d="M5 3h4l2 5-3 2a11 11 0 0 0 6 6l2-3 5 2v4a2 2 0 0 1-2 2A18 18 0 0 1 3 5a2 2 0 0 1 2-2z"/></svg>
    1-800-555-0142
  </div>
  <div class="contact contact-web">
    <svg width="20" height="20" viewBox="0 0 24 24" fill="none" stroke="#fbed22" stroke-width="1.5"><circle cx="12" cy="12" r="10"/><path d="M2 12h20M12 2c3 3 3 17 0 20M12 2c-3 3-3 17 0 20"/></svg>
    www.brokaleaf.net
  </div>
  <div class="contact contact-mail">
    <svg width="20" height="14" viewBox="0 0 24 16" fill="none" stroke="#fbed22" stroke-width="1.5"><rect x="1" y="1" width="22" height="14"/><path d="M1 1l11 8 11-8"/></svg>
    info@brokaleaf.net
  </div>

  <div class="brand-name">BROKALEAF</div>
  <div class="tagline">Neuromuscular Support<br>Natural Muscle &amp; Joint Formula</div>

  <ul class="key-ingredients">
    <li><svg width="12" height="10" viewBox="0 0 12 10" fill="none" stroke="#fbed22" stroke-width="2"><path d="M1 5l3.5 3.5L11 1"/></svg>Tumeric <small>(extract 95% Curcuminoids)</small></li>
    <li><svg width="12" height="10" viewBox="0 0 12 10" fill="none" stroke="#fbed22" stroke-width="2"><path d="M1 5l3.5 3.5L11 1"/></svg>Boswellia <small>(extract 65% Boswellic Acids)</small></li>
    <li><svg width="12" height="10" viewBox="0 0 12 10" fill="none" stroke="#fbed22" stroke-width="2"><path d="M1 5l3.5 3.5L11 1"/></svg>Bromelain</li>
    <li><svg width="12" height="10" viewBox="0 0 12 10" fill="none" stroke="#fbed22" stroke-width="2"><path d="M1 5l3.5 3.5L11 1"/></svg>Quercetin</li>
  </ul>

  <div class="claims">
    <div class="claim"></div><div class="claim"></div><div class="claim"></div>
  </div>

  <div class="count"><b>60</b> Capsules</div>

  <div class="facts">
    <h2>SUPPLEMENT FACTS</h2>
    <div class="serving">Serving Size: 1 capsule</div>
    <div class="facts-row facts-head"><span>Amount Per Serving</span><span></span><span>%DV</span></div>
    <div class="facts-row"><span>Thiamin (as thiamin hydrochloride USP</span><span>25mg</span><span>1667%</span></div>
    <div class="facts-row"><span>Vitamin B6 (as pyridox, ne hycrochloride USP)</span><span>25mg</span><span>1667%</span></div>
    <div class="facts-row"><span>DLPA (DL-Phenylalanine)</span><span>75mg</span><span>*</span></div>
    <div class="facts-row"><span>Turmeric (Curcuma longa) root, dried extract,<br>dried extract, min 95% curcuminoids</span><span>200mg</span><span>*</span></div>
    <div class="facts-row"><span>Boswellia serrata gum resin, dried extract,<br>min 65% boswellic acids</span><span>175mg</span><span>*</span></div>
    <div class="facts-row"><span>Bromelain (from pineapple)</span><span>125mg</span><span>*</span></div>
    <div class="facts-row" style="border-bottom:0"><span>Quercetin (as quercetin dehydrate)</span><span>75mg</span><span>*</span></div>
    <div class="facts-note">*Daily Value not established</div>
  </div>

  <div class="other">Other Ingredients: Vegetarian Capsules</div>

  <div class="band">
    <span class="band-natural">100% ALL NATURAL</span>
    <span class="band-type">Dietary Supplement</span>
    <span class="band-patent">Patenet No. 5204318</span>
  </div>
</section>
</body>
</html>
```